Partlow Law Stationery - Letterhead, Envelopes, Business Cards

We need high quality business stationery for our Personal Injury Law Firm located in Houston, Texas. The design should include the logo, Partlow Law Group, PLLC, 713-555-0148, 2750 Marlowe Crescent, Suite 318, Houston, Texas 77099 www.PartlowLaw.example. The colors are blue and white. The letterhead should also include the Attorneys - Marcy Teague, Everett K. Partlow and Dorian Fisk.

```html
<!DOCTYPE html>
<html lang="en">
<head>
<meta charset="utf-8">
<title>Partlow Law Stationery</title>
<link href="https://fonts.googleapis.com/css2?family=Lato:wght@400;700&family=Raleway:wght@600&display=swap" rel="stylesheet">
<style>
  :root {
    --navy: #001a3d;
    --white: #ffffff;
    --backdrop: #a0a0a0;
    --ink: #2a2a2a;
    --faint: #e3e6ec;
  }
  * { margin: 0; padding: 0; box-sizing: border-box; }
  html, body { width: 1200px; height: 857px; overflow: hidden; }
  body {
    background: var(--backdrop);
    font-family: "Lato", sans-serif;
    position: relative;
  }
  .sheet { position: absolute; background: var(--white); overflow: hidden; }
  .wave { position: absolute; left: 0; top: 0; }

  .mark {
    position: absolute;
    border-radius: 50%;
    background: var(--navy);
    color: var(--white);
    display: flex;
    align-items: center;
    justify-content: center;
    text-align: center;
    font-family: "Lato", sans-serif;
    font-weight: 700;
    line-height: 1.05;
  }
  .mark--ringed { box-shadow: 0 0 0 5px var(--white), 0 2px 6px 5px rgba(0,0,0,0.18); }
  .mark--faint {
    background: transparent;
    border: 10px solid var(--faint);
    color: var(--faint);
  }

  /* Letterhead */
  .letterhead { left: 69px; top: 82px; width: 475px; height: 668px; }
  .letterhead .mark--logo { left: 75px; top: 8px; width: 94px; height: 94px; font-size: 15px; }
  .contact-list { position: absolute; left: 298px; top: 17px; list-style: none; color: var(--white); font-size: 10px; line-height: 1.2; }
  .contact-list li { display: flex; align-items: flex-start; gap: 7px; margin-bottom: 4px; }
  .contact-list svg { flex: none; margin-top: 1px; }
  .letterhead .mark--watermark { left: 110px; top: 203px; width: 306px; height: 306px; font-size: 52px; border-width: 14px; }
  .letterhead-footer { position: absolute; left: 0; bottom: 0; width: 475px; height: 46px; background: var(--navy); }
  .footer-firm { position: absolute; left: 18px; top: 9px; color: var(--white); line-height: 1.35; }
  .footer-firm strong { display: block; font-weight: 700; font-size: 9.5px; letter-spacing: 0.3px; }
  .footer-firm span { display: block; font-size: 8px; }
  .footer-seal-box { position: absolute; left: 338px; bottom: -4px; width: 59px; height: 54px; background: var(--white); }
  .letterhead .mark--footer { left: 343px; top: 627px; width: 48px; height: 48px; font-size: 9px; }

  /* Envelope */
  .envelope { left: 582px; top: 211px; width: 543px; height: 235px; }
  .envelope .mark--logo { left: 45px; top: 24px; width: 110px; height: 110px; font-size: 19px; }
  .envelope-address { position: absolute; left: 40px; top: 156px; font-size: 10.5px; color: var(--ink); line-height: 1.15; }
  .envelope .mark--watermark { left: 342px; top: 12px; width: 200px; height: 200px; font-size: 34px; }
  .envelope-band { position: absolute; left: 0; bottom: 0; width: 100%; height: 6px; background: var(--navy); }

  /* Business cards */
  .card-front { left: 602px; top: 469px; width: 201px; height: 114px; }
  .card-front .mark--logo { left: 26px; top: 5px; width: 40px; height: 40px; font-size: 7px; box-shadow: 0 0 0 3px var(--white), 0 1px 4px 3px rgba(0,0,0,0.18); }
  .card-name { position: absolute; right: 10px; top: 13px; text-align: right; color: var(--white); }
  .card-name strong { display: block; font-family: "Raleway", sans-serif; font-weight: 600; font-size: 9px; }
  .card-name span { display: block; font-size: 4.5px; margin-top: 1px; }
  .card-rule { position: absolute; left: 11px; top: 74px; width: 177px; height: 0; border-top: 0.6px solid #444; }
  .card-contacts { position: absolute; left: 10px; top: 79px; list-style: none; font-size: 5px; color: var(--ink); }
  .card-contacts li { display: flex; align-items: center; gap: 3px; margin-bottom: 4px; }
  .card-address { position: absolute; right: 13px; top: 82px; font-size: 5px; text-align: right; color: var(--ink); line-height: 1.3; }
  .card-band { position: absolute; left: 0; bottom: 0; width: 100%; height: 9px; background: var(--navy); }
  .card-seal { position: absolute; left: 150px; top: 104px; width: 11px; height: 11px; border-radius: 50%; background: var(--navy); box-shadow: 0 0 0 1px var(--white); }

  .card-back { left: 816px; top: 469px; width: 200px; height: 114px; background: var(--navy); }
  .card-back .mark--logo { left: 66px; top: 23px; width: 68px; height: 68px; font-size: 12px; box-shadow: 0 0 0 3px var(--white), 0 3px 6px 3px rgba(0,0,0,0.35); }
</style>
</head>
<body>

  <section class="sheet letterhead" aria-label="Letterhead">
    <svg class="wave" width="475" height="110" viewBox="0 0 475 110" aria-hidden="true">
      <path d="M0,0 H475 V94 C420,101 340,104 250,80 C190,62 150,40 95,34 C60,30 25,36 0,40 Z" fill="var(--navy)"/>
      <path d="M0,14 C50,4 110,6 160,22" stroke="var(--white)" stroke-width="5" fill="none"/>
      <path d="M0,31 C50,22 110,24 170,45 C200,56 220,70 260,84" stroke="var(--white)" stroke-width="4" fill="none"/>
      <path d="M120,95 C210,104 330,110 475,96" stroke="var(--navy)" stroke-width="2.5" fill="none"/>
    </svg>
    <div class="mark mark--logo mark--ringed">Partlow<br>Law</div>
    <ul class="contact-list">
      <li>
        <svg width="9" height="9" viewBox="0 0 24 24" aria-hidden="true"><path d="M6.6 10.8a15 15 0 0 0 6.6 6.6l2.2-2.2a1 1 0 0 1 1-.25 11 11 0 0 0 3.6.6 1 1 0 0 1 1 1V20a1 1 0 0 1-1 1A17 17 0 0 1 3 4a1 1 0 0 1 1-1h3.5a1 1 0 0 1 1 1c0 1.25.2 2.45.6 3.6a1 1 0 0 1-.25 1z" fill="var(--white)"/></svg>
        <span>713-555-0148</span>
      </li>
      <li>
        <svg width="9" height="9" viewBox="0 0 24 24" aria-hidden="true"><circle cx="12" cy="12" r="9" fill="none" stroke="var(--white)" stroke-width="2"/><path d="M3 12h18M12 3c3 3 3 15 0 18M12 3c-3 3-3 15 0 18" fill="none" stroke="var(--white)" stroke-width="1.6"/></svg>
        <span>www.PartlowLaw.example</span>
      </li>
      <li>
        <svg width="9" height="11" viewBox="0 0 24 30" aria-hidden="true"><path d="M12 0a10 10 0 0 0-10 10c0 8 10 20 10 20s10-12 10-20A10 10 0 0 0 12 0zm0 14a4 4 0 1 1 0-8 4 4 0 0 1 0 8z" fill="var(--white)"/></svg>
        <span>2750 Marlowe Crescent,<br>Suite 318, Houston, Texas 77099</span>
      </li>
    </ul>
    <div class="mark mark--faint mark--watermark">Partlow<br>Law</div>
    <div class="letterhead-footer">
      <div class="footer-firm">
        <strong>Partlow Law Group, PLLC</strong>
        <span>Marcy Teague &nbsp;·&nbsp; Everett K. Partlow &nbsp;·&nbsp; Dorian Fisk</span>
      </div>
    </div>
    <div class="footer-seal-box"></div>
    <div class="mark mark--footer">Partlow<br>Law</div>
  </section>

  <section class="sheet envelope" aria-label="Envelope">
    <div class="mark mark--logo">Partlow<br>Law</div>
    <p class="envelope-address">2750 Marlowe Crescent,<br>Suite 318, Houston, Texas 77099</p>
    <div class="mark mark--faint mark--watermark">Partlow<br>Law</div>
    <div class="envelope-band"></div>
  </section>

  <section class="sheet card-front" aria-label="Business card front">
    <svg class="wave" width="201" height="48" viewBox="0 0 201 48" aria-hidden="true">
      <path d="M0,0 H201 V38 C170,44 130,44 95,30 C70,20 40,12 0,15 Z" fill="var(--navy)"/>
      <path d="M0,6 C30,1 60,2 85,12" stroke="var(--white)" stroke-width="2.5" fill="none"/>
      <path d="M0,13 C35,7 70,10 100,28" stroke="var(--white)" stroke-width="2" fill="none"/>
      <path d="M60,38 C110,47 160,48 201,41" stroke="var(--navy)" stroke-width="1.2" fill="none"/>
    </svg>
    <div class="mark mark--logo">Partlow<br>Law</div>
    <div class="card-name"><strong>Colin Harwick</strong><span>Managing Director</span></div>
    <div class="card-rule"></div>
    <ul class="card-contacts">
      <li>
        <svg width="5" height="5" viewBox="0 0 24 24" aria-hidden="true"><path d="M6.6 10.8a15 15 0 0 0 6.6 6.6l2.2-2.2a1 1 0 0 1 1-.25 11 11 0 0 0 3.6.6 1 1 0 0 1 1 1V20a1 1 0 0 1-1 1A17 17 0 0 1 3 4a1 1 0 0 1 1-1h3.5a1 1 0 0 1 1 1c0 1.25.2 2.45.6 3.6a1 1 0 0 1-.25 1z" fill="var(--navy)"/></svg>
        <span>713-555-0148</span>
      </li>
      <li>
        <svg width="5" height="5" viewBox="0 0 24 24" aria-hidden="true"><circle cx="12" cy="12" r="9" fill="none" stroke="var(--navy)" stroke-width="2.5"/><path d="M3 12h18M12 3v18" stroke="var(--navy)" stroke-width="2"/></svg>
        <span>www.PartlowLaw.example</span>
      </li>
    </ul>
    <p class="card-address">2750 Marlowe Crescent,<br>Suite 318, Houston, Texas 77099</p>
    <div class="card-band"></div>
    <div class="card-seal"></div>
  </section>

  <section class="sheet card-back" aria-label="Business card back">
    <div class="mark mark--logo">Partlow<br>Law</div>
  </section>

</body>
</html>
```